Tallow Crest Business Card

We need a business card designed for a a company called "Tallow Crest". We offer consulting, coaching and training to business leaders and coaches (across the world) using the latest findings in neuroscience, social and emotional intelligence and positive psychology. The final design should communicate the use of brain science to create sustainable relationships.

The card should be doublesided. The logo is attached and names and titles will be provided to the successful designer. Thank you.

Industry/Entity Type

Training

```html
<!DOCTYPE html>
<html lang="en">
<head>
<meta charset="utf-8">
<title>Tallow Crest Business Card</title>
<link rel="stylesheet" href="https://fonts.googleapis.com/css2?family=Arimo:wght@400;700&display=swap">
<style>
  :root {
    --stage: #e4e5e6;
    --card: #1d1c1e;
    --blue: #1b8fc6;
    --green: #a8c934;
    --text: #e8e8e8;
  }
  * { box-sizing: border-box; margin: 0; padding: 0; }
  html, body { width: 1200px; height: 900px; overflow: hidden; }
  body {
    background: var(--stage);
    font-family: "Arimo", Arial, sans-serif;
    display: flex;
    flex-direction: column;
    align-items: center;
    justify-content: center;
    gap: 40px;
  }
  .card {
    position: relative;
    width: 630px;
    height: 360px;
    background: var(--card);
    overflow: hidden;
    box-shadow: 0 6px 18px rgba(0,0,0,.25);
  }
  .card-front {
    display: flex;
    flex-direction: column;
    align-items: center;
    justify-content: center;
    gap: 14px;
  }
  .brand {
    display: flex;
    align-items: center;
    gap: 12px;
    font-weight: 700;
    color: var(--blue);
    letter-spacing: 1px;
  }
  .brand-mark {
    background: var(--green);
    border-radius: 50%;
  }
  .card-front .brand { font-size: 46px; }
  .card-front .brand-mark { width: 30px; height: 30px; }
  .front-web {
    color: var(--green);
    font-size: 15px;
    letter-spacing: 2px;
  }
  .accent-bar {
    position: absolute;
    top: 40px;
    right: 0;
    width: 80px;
    height: 26px;
    background: var(--green);
  }
  .accent-block {
    position: absolute;
    left: 56px;
    bottom: 40px;
    width: 92px;
    height: 128px;
    background: var(--blue);
  }
  .card-back .brand {
    position: absolute;
    left: 110px;
    top: 78px;
    font-size: 40px;
  }
  .card-back .brand-mark { width: 26px; height: 26px; }
  .holder {
    position: absolute;
    left: 176px;
    top: 160px;
    color: var(--green);
    font-size: 22px;
    font-weight: 700;
  }
  .contacts {
    position: absolute;
    left: 176px;
    top: 196px;
    right: 30px;
    display: grid;
    grid-template-columns: auto auto;
    column-gap: 26px;
    row-gap: 9px;
    list-style: none;
    color: var(--text);
    font-size: 14px;
  }
  .contacts li { display: flex; align-items: center; gap: 8px; white-space: nowrap; }
  .contacts li.wide { grid-column: 1 / -1; }
  .contacts svg { width: 14px; height: 14px; fill: var(--green); flex: none; }
</style>
</head>
<body>
  <section class="card card-front" aria-label="Card front">
    <div class="brand"><span class="brand-mark"></span>Tallow Crest</div>
    <p class="front-web">www.tallowcrest.com.au</p>
  </section>

  <section class="card card-back" aria-label="Card back">
    <div class="accent-bar"></div>
    <div class="brand"><span class="brand-mark"></span>Tallow Crest</div>
    <h1 class="holder">Marcus Ellery</h1>
    <div class="accent-block"></div>
    <ul class="contacts">
      <li>
        <svg viewBox="0 0 16 16"><path d="M3 2h3l1.5 3.5-2 1.2a8 8 0 0 0 3.8 3.8l1.2-2L14 10v3a1 1 0 0 1-1 1A11 11 0 0 1 2 3a1 1 0 0 1 1-1z"/></svg>
        0400 555 120
      </li>
      <li>
        <svg viewBox="0 0 16 16"><path d="M1 3h14v10H1z M2 4.2v.6l6 4 6-4v-.6z" fill-rule="evenodd"/></svg>
        marcus@tallowcrest.com.au
      </li>
      <li>
        <svg viewBox="0 0 16 16"><path d="M4 1h8a1 1 0 0 1 1 1v12a1 1 0 0 1-1 1H4a1 1 0 0 1-1-1V2a1 1 0 0 1 1-1zm1 2v8h6V3zm3 9.2a.9.9 0 1 0 0 1.8.9.9 0 0 0 0-1.8z" fill-rule="evenodd"/></svg>
        0400 555 120
      </li>
      <li>
        <svg viewBox="0 0 16 16"><path d="M8 1a7 7 0 1 0 0 14A7 7 0 0 0 8 1zm0 1.5c.8 0 1.8 1.7 2 4.5H6c.2-2.8 1.2-4.5 2-4.5zM2.6 7h2c.1-1.6.4-3 .9-4A5.5 5.5 0 0 0 2.6 7zm8.8 0h2a5.5 5.5 0 0 0-2.9-4c.5 1 .8 2.4.9 4zM2.6 9a5.5 5.5 0 0 0 2.9 4c-.5-1-.8-2.4-.9-4zm3.4 0c.2 2.8 1.2 4.5 2 4.5s1.8-1.7 2-4.5zm5.4 0c-.1 1.6-.4 3-.9 4a5.5 5.5 0 0 0 2.9-4z" fill-rule="evenodd"/></svg>
        www.tallowcrest.com.au
      </li>
      <li class="wide">
        <svg viewBox="0 0 16 16"><path d="M8 1a5 5 0 0 0-5 5c0 3.5 5 9 5 9s5-5.5 5-9a5 5 0 0 0-5-5zm0 3a2 2 0 1 1 0 4 2 2 0 0 1 0-4z" fill-rule="evenodd"/></svg>
        12 Harbour Lane, Suite 200, Ashby, NC 00000
      </li>
    </ul>
  </section>
</body>
</html>
```